Business Card Design

Electronic Security Installation Specialists

Check out our website at www.brightpulsellc.com to see what we do.

Industry/Entity Type

Business

Contact Information for Business Card

Bright Pulse
Marianne Tolbert
218 Orchard Bend
Shepherdstow, WV 25443

Colors
3176b5
0455a3
ffffff

```html
<!DOCTYPE html>
<html lang="en">
<head>
<meta charset="utf-8">
<title>Bright Pulse – Business Card</title>
<link rel="stylesheet" href="https://fonts.googleapis.com/css2?family=Open+Sans:wght@400;600;700&display=swap">
<style>
  :root {
    --backdrop: #e6e8eb;
    --card-light: #ffffff;
    --card-shade: #e4e5e8;
    --brand-blue: #0455a3;
    --brand-blue-light: #3176b5;
    --swoosh-dark: #6e7075;
    --swoosh-light: #c9cbcf;
    --ink: #3a3b3f;
    --white: #ffffff;
  }
  * { margin: 0; padding: 0; box-sizing: border-box; }
  html, body {
    width: 1200px; height: 900px; overflow: hidden;
    background: var(--backdrop);
    font-family: "Open Sans", Arial, sans-serif;
  }
  .card {
    position: absolute; left: 100px; top: 165px;
    width: 1000px; height: 570px;
    border-radius: 48px; overflow: hidden;
    background: linear-gradient(160deg, var(--card-light) 40%, var(--card-shade) 100%);
    box-shadow: 0 14px 40px rgba(0,0,0,0.18);
  }
  .card-waves { position: absolute; inset: 0; width: 1000px; height: 570px; }
  .brand {
    position: absolute; right: 58px; top: 200px;
    display: flex; align-items: center; gap: 16px;
  }
  .brand-dot {
    width: 34px; height: 34px; border-radius: 50%;
    background: var(--brand-blue);
  }
  .brand-name {
    font-size: 40px; font-weight: 600; color: var(--brand-blue);
    letter-spacing: 0.5px; white-space: nowrap;
  }
  .contact-list {
    position: absolute; left: 48px; top: 282px;
    list-style: none; color: var(--white);
    font-size: 19px; line-height: 1.25;
  }
  .contact-item { display: flex; align-items: flex-start; gap: 12px; margin-bottom: 8px; }
  .contact-icon { flex: 0 0 20px; width: 20px; height: 20px; margin-top: 2px; }
  .person {
    position: absolute; right: 92px; top: 420px; text-align: right; color: var(--ink);
    white-space: nowrap;
  }
  .person-name { font-size: 34px; font-weight: 700; line-height: 1.2; }
  .person-title { font-size: 27px; font-weight: 400; }
</style>
</head>
<body>
  <div class="card">
    <svg class="card-waves" viewBox="0 0 1000 570" aria-hidden="true">
      <defs>
        <linearGradient id="swooshGrad" x1="0" y1="0" x2="1" y2="0">
          <stop offset="0" stop-color="var(--swoosh-dark)"/>
          <stop offset="0.5" stop-color="var(--swoosh-light)"/>
          <stop offset="1" stop-color="var(--swoosh-dark)"/>
        </linearGradient>
        <radialGradient id="blueGrad" cx="0.3" cy="0.5" r="0.8">
          <stop offset="0" stop-color="var(--brand-blue-light)"/>
          <stop offset="1" stop-color="var(--brand-blue)"/>
        </radialGradient>
      </defs>
      <path d="M0,140 C260,105 370,190 460,345 C545,490 650,560 790,570 L0,570 Z" fill="url(#swooshGrad)"/>
      <path d="M0,160 C255,128 355,210 445,360 C525,495 625,560 760,570 L0,570 Z" fill="var(--card-light)"/>
      <path d="M0,176 C250,148 340,228 430,372 C505,498 600,560 735,570 L0,570 Z" fill="url(#swooshGrad)"/>
      <path d="M0,186 C248,160 332,240 420,382 C495,502 590,562 720,570 L0,570 Z" fill="url(#blueGrad)"/>
    </svg>

    <div class="brand">
      <span class="brand-dot"></span>
      <span class="brand-name">Bright Pulse</span>
    </div>

    <ul class="contact-list">
      <li class="contact-item">
        <svg class="contact-icon" viewBox="0 0 20 20"><circle cx="10" cy="10" r="10" fill="var(--white)"/><path d="M10 4a4 4 0 0 0-4 4c0 3 4 8 4 8s4-5 4-8a4 4 0 0 0-4-4z" fill="var(--brand-blue)"/></svg>
        <span>218 Orchard Bend,<br>Shepherdstow, WV 25443</span>
      </li>
      <li class="contact-item">
        <svg class="contact-icon" viewBox="0 0 20 20"><circle cx="10" cy="10" r="10" fill="var(--white)"/><path d="M6 5l2.5-.5 1.2 3-1.5 1a7 7 0 0 0 3.3 3.3l1-1.5 3 1.2-.5 2.5C10 15 5 10 6 5z" fill="var(--brand-blue)"/></svg>
        <span>304-555-0142</span>
      </li>
      <li class="contact-item">
        <svg class="contact-icon" viewBox="0 0 20 20"><circle cx="10" cy="10" r="10" fill="var(--white)"/><rect x="7" y="4" width="6" height="12" rx="1.5" fill="var(--brand-blue)"/></svg>
        <span>304-555-0178</span>
      </li>
      <li class="contact-item">
        <svg class="contact-icon" viewBox="0 0 20 20"><circle cx="10" cy="10" r="10" fill="var(--white)"/><rect x="5" y="8" width="10" height="7" fill="var(--brand-blue)"/><rect x="7" y="5" width="6" height="3" fill="var(--brand-blue)"/></svg>
        <span>304-555-0193</span>
      </li>
      <li class="contact-item">
        <svg class="contact-icon" viewBox="0 0 20 20"><circle cx="10" cy="10" r="10" fill="var(--white)"/><rect x="4.5" y="6" width="11" height="8" fill="var(--brand-blue)"/><path d="M4.5 6l5.5 4.5L15.5 6" fill="none" stroke="var(--white)" stroke-width="1"/></svg>
        <span>hello@brightpulsellc.com</span>
      </li>
      <li class="contact-item">
        <svg class="contact-icon" viewBox="0 0 20 20"><circle cx="10" cy="10" r="10" fill="var(--white)"/><circle cx="10" cy="10" r="5.5" fill="none" stroke="var(--brand-blue)" stroke-width="1.4"/><path d="M4.5 10h11M10 4.5c-3 3-3 8 0 11M10 4.5c3 3 3 8 0 11" fill="none" stroke="var(--brand-blue)" stroke-width="1"/></svg>
        <span>www.brightpulsellc.com</span>
      </li>
    </ul>

    <div class="person">
      <p class="person-name">Marianne Tolbert</p>
      <p class="person-title">Owner / C.E.O</p>
    </div>
  </div>
</body>
</html>
```